Flyer for the Radiant Harvest Worship Day

I am looking to create a flyer for a one day prayer retreat our church is organizing.
This flyer will be posted on social media, websites and will also be printed so it can be mailed to people.
I am looking for something professional, with good use of our logo and band colors (logo colors).
I am counting on the designer's skill, creativity, art and knowledge of media communication to produce a flyer that will effectively and quickly convey the message we are trying to spread.
CONTENT OF THE FLYER:
Event title: Radiant Harvest Worship Day
Date: Tuesday July 2nd, 2019
Time: 11:00AM - 7:00PM
Bellmont Hotel, 4815 Alder Lane, Portland, Maine 04117 (Room: Willowmere)
Event Key words to highlight what the event is about: Prayer, Sharing the Word, Panel discussion, prophecy, Impartation.
Key phrases:
A one day prayer retreat.
Jesus Chris is Lord
Contact info:
www.tovelin.org
Phone: 207 555 0193
Email: contact@brookhavenfold.org

```html
<!DOCTYPE html>
<html lang="en">
<head>
<meta charset="utf-8">
<title>Radiant Harvest Worship Day</title>
<link rel="stylesheet" href="https://fonts.googleapis.com/css2?family=Bebas+Neue&family=Great+Vibes&family=Yellowtail&family=Montserrat:wght@900&family=Tinos&family=Arimo&display=swap">
<style>
  :root {
    --navy-deep: #0a2e55;
    --navy: #0f4272;
    --navy-box: #0b3560;
    --sky: #7fd3ef;
    --sky-text: #8fdcf2;
    --orange: #f5a01a;
    --gold: #f2c417;
    --white: #ffffff;
  }
  * { margin: 0; padding: 0; box-sizing: border-box; }
  html, body { width: 857px; height: 1200px; overflow: hidden; background: var(--navy-deep); }
  .flyer {
    position: relative; width: 857px; height: 1200px; overflow: hidden;
    background: radial-gradient(ellipse at 70% 35%, var(--navy) 0%, var(--navy-deep) 75%);
  }
  .artwork-christ {
    position: absolute; left: -40px; top: 0; width: 540px; height: 1040px;
    background: radial-gradient(closest-side, rgba(214,222,230,.7) 0%, rgba(150,170,190,.4) 45%, rgba(15,66,114,0) 100%);
  }
  .artwork-bible {
    position: absolute; left: 80px; top: 800px; width: 777px; height: 360px;
    background: radial-gradient(closest-side, rgba(210,200,170,.3) 0%, rgba(15,66,114,0) 100%);
  }
  .artwork-hands {
    position: absolute; left: 596px; top: 282px; width: 184px; height: 226px;
    border-radius: 40% 40% 30% 30%;
    background: radial-gradient(ellipse at 50% 40%, #f1cfa8 0%, #d9a070 45%, rgba(200,60,40,.6) 75%, rgba(15,66,114,0) 100%);
  }
  .retreat-tag {
    position: absolute; left: 342px; top: 38px; width: 444px; height: 74px;
    background: var(--orange); color: var(--white); white-space: nowrap; overflow: hidden;
    font: 50px/74px "Bebas Neue", "Oswald", sans-serif; text-align: center;
  }
  .lord-line {
    position: absolute; left: 330px; top: 124px; width: 527px; text-align: center; white-space: nowrap;
    font: 60px/1 "Great Vibes", cursive; color: var(--sky);
    text-shadow: 2px 3px 4px rgba(0,0,0,.6);
  }
  .title-bubble { position: absolute; left: 230px; top: 342px; width: 385px; height: 113px; }
  .event-title {
    position: absolute; left: 210px; top: 358px; width: 420px; white-space: nowrap;
    font-family: "Montserrat", sans-serif; font-weight: 900; color: var(--white);
    text-shadow: 3px 4px 4px rgba(0,0,0,.55); line-height: 1;
  }
  .event-title .word-1 { display: block; font-size: 58px; letter-spacing: -2px; }
  .event-title .word-2 { display: block; font-size: 58px; letter-spacing: -2px; text-align: right; margin-top: 6px; }
  .event-script {
    position: absolute; left: 290px; top: 494px; width: 540px; text-align: center; white-space: nowrap;
    font: 80px/1 "Yellowtail", cursive; color: var(--gold);
    text-shadow: 2px 3px 3px rgba(0,0,0,.6);
  }
  .keywords {
    position: absolute; left: 100px; top: 630px; width: 740px; text-align: center; white-space: nowrap;
    font: 42px/50px "Bebas Neue", sans-serif; color: var(--white);
  }
  .details {
    position: absolute; left: 40px; top: 742px; width: 760px; text-align: center; white-space: nowrap;
    font: 32px/41px "Tinos", serif; color: var(--sky-text);
    text-shadow: 0 0 4px rgba(0,0,0,.6);
  }
  .contact {
    position: absolute; left: 100px; top: 996px; width: 340px; text-align: center; white-space: nowrap;
    font: 19px/23.5px "Arimo", sans-serif; color: var(--white);
  }
  .brand-box {
    position: absolute; left: 505px; top: 918px; width: 302px; height: 245px;
    background: var(--navy-box);
    display: flex; align-items: center; justify-content: center; gap: 12px;
  }
  .brand-dot { width: 20px; height: 20px; border-radius: 50%; background: var(--orange); }
  .brand-name { font: 50px/1 "Tinos", serif; color: var(--white); letter-spacing: 1px; }
</style>
</head>
<body>
<main class="flyer">
  <div class="artwork-christ" role="img" aria-label="Soft painted portrait of Christ with open hands, fading into blue"></div>
  <div class="artwork-bible" role="img" aria-label="Open Bible with praying hands in soft light"></div>

  <div class="retreat-tag">A One Day Prayer Retreat</div>
  <div class="lord-line">Jesus Christ is Lord</div>

  <svg class="title-bubble" viewBox="0 0 385 113" aria-hidden="true">
    <defs>
      <radialGradient id="bubbleFill" cx="50%" cy="40%" r="60%">
        <stop offset="0" stop-color="#6cc4f0"/>
        <stop offset="1" stop-color="#2378bd"/>
      </radialGradient>
    </defs>
    <ellipse cx="192" cy="56" rx="190" ry="54" fill="url(#bubbleFill)"/>
  </svg>

  <div class="artwork-hands" role="img" aria-label="Illustration of praying hands with red and yellow sleeve"></div>

  <h1 class="event-title">
    <span class="word-1">RADIANT</span>
    <span class="word-2">HARVEST</span>
  </h1>
  <div class="event-script">Worship day</div>

  <p class="keywords">Prayer – Sharing the Word – Panel Discussion<br>Prophecy – Impartation</p>

  <p class="details">
    Date : Tuesday, July 2nd, 2019<br>
    Time : 11.00 am - 07.00 pm<br>
    Venue: Bellmont Hotel 4815 Alder Lane<br>
    Portland, Maine 04117 (Room Willowmere)
  </p>

  <p class="contact">
    Contact info :<br>
    www.tovelin.org<br>
    Phone : 207 555 0193<br>
    email : contact@brookhavenfold.org
  </p>

  <div class="brand-box">
    <span class="brand-dot"></span>
    <span class="brand-name">TOVELIN</span>
  </div>
</main>
</body>
</html>
```